Website for Apartment Rental in Prague

I would like to create designs of my website focused on luxury apartment rentals in Prague, Czech Republic. I created initial mock-ups, They are all attached. I need to design homepage and subpage. The mock-ups were created by combining elements from different websites that I liked but I need you to create a design that is unique and original. The attached files a only a guidance for the structure of the website but not for the design. Try to be creative.

Industry/Entity Type

Apartment

```html
<!DOCTYPE html>
<html lang="en">
<head>
<meta charset="utf-8">
<title>Vltava Suites – Apartments &amp; Rates</title>
<link rel="stylesheet" href="https://fonts.googleapis.com/css2?family=Montserrat:wght@400;600;700&family=Open+Sans:wght@400;600&display=swap">
<style>
:root{
  --ink:#2a2a2a;
  --dark:#1f1f1f;
  --darker:#141414;
  --gold:#d4a257;
  --paper:#ffffff;
  --mist:#f1f1f1;
  --line:#d8d8d8;
  --panel-head:#4a4a4a;
}
*{box-sizing:border-box;margin:0;padding:0}
html,body{width:1200px;height:2436px;overflow:hidden}
body{position:relative;background:var(--mist);font-family:"Open Sans",Arial,sans-serif;color:var(--ink);font-size:14px}
.abs{position:absolute}
/* top bar */
.topbar{left:0;top:0;width:1200px;height:40px;background:var(--dark);color:#ddd;font-size:13px;display:flex;align-items:center;padding:0 110px;gap:40px}
.topbar .item{display:flex;align-items:center;gap:8px;white-space:nowrap}
.topbar .spacer{flex:1}
.topbar .socials{display:flex;gap:14px}
.dot{width:12px;height:12px;border-radius:50%;background:#bbb;display:inline-block}
/* nav */
.nav{left:0;top:40px;width:1200px;height:140px;background:var(--paper);display:flex;align-items:center;justify-content:center;gap:48px;font-family:"Montserrat",sans-serif;font-weight:600;font-size:17px;letter-spacing:.5px}
.nav a{color:var(--ink);text-decoration:none}
.brand{display:flex;align-items:center;gap:10px;margin:0 40px;font-family:"Montserrat",sans-serif;font-weight:700;font-size:30px;color:var(--gold);text-transform:uppercase;line-height:1;white-space:nowrap}
.brand .sq{width:22px;height:22px;background:var(--gold);flex:none}
/* hero */
.hero{left:0;top:180px;width:1200px;height:292px;background:linear-gradient(180deg,#8a8886 0%,#c7c1b8 45%,#e6e2dc 100%)}
.booking{left:120px;top:352px;width:984px;height:120px;background:var(--paper);box-shadow:0 4px 14px rgba(0,0,0,.18);padding:18px 28px;display:flex;align-items:flex-end;gap:18px}
.field{display:flex;flex-direction:column;gap:6px;font-size:13px;font-weight:600}
.field .box{height:30px;border:1px solid var(--line);background:#fafafa;display:flex;align-items:center;justify-content:flex-end;padding:0 8px}
.field.first{font-family:"Montserrat",sans-serif;font-size:17px;font-weight:700}
.btn{font-family:"Montserrat",sans-serif;font-weight:600;font-size:13px;color:#fff;display:flex;align-items:center;justify-content:center;letter-spacing:.5px;white-space:nowrap}
.btn.gold{background:var(--gold)}
.btn.dark{background:var(--panel-head)}
/* steps */
.steps{left:112px;top:488px;width:1008px;height:48px;background:var(--paper);display:flex;align-items:center;justify-content:space-around;font-family:"Montserrat",sans-serif;font-weight:600;font-size:14px;border-bottom:3px solid var(--line)}
/* sidebar */
.panel{left:112px;width:268px;background:var(--paper);border:1px solid var(--line)}
.panel h3{background:var(--panel-head);color:#fff;font-family:"Montserrat",sans-serif;font-size:17px;padding:10px 14px;letter-spacing:.5px}
.panel .body{padding:12px 16px;font-size:14px;line-height:1.55}
.linkline{text-align:right;font-size:13px;text-decoration:underline}
.mini-photo{height:150px;background:linear-gradient(135deg,#9a9590,#d8d2c8 60%,#4f7a75)}
.map{height:180px;background:linear-gradient(135deg,#f3efe6,#e4dfd3 55%,#c9d8e3)}
.search{display:flex;gap:8px;margin-top:10px}
.search .in{flex:1;height:28px;border:1px solid var(--line)}
/* listings */
.listing{left:388px;width:732px;height:340px}
.photo{position:absolute;left:0;top:0;width:300px;height:240px;background:linear-gradient(160deg,#6f6b67 0%,#bfb8ad 40%,#e3ddd3 70%,#3f7c77 100%)}
.tag{position:absolute;left:0;bottom:0;background:var(--gold);color:#fff;font-family:"Montserrat",sans-serif;font-weight:700;font-size:12px;padding:6px 12px}
.arrow{position:absolute;top:104px}
.thumbs{position:absolute;left:0;top:252px;display:flex;gap:8px}
.thumbs div{width:69px;height:62px;background:linear-gradient(160deg,#7a7570,#cfc8bd 60%,#4a7d78)}
.details{position:absolute;left:324px;top:0;width:408px;height:260px}
.details h2{font-family:"Montserrat",sans-serif;font-size:22px;font-weight:700;padding-bottom:10px;border-bottom:2px solid var(--ink);white-space:nowrap}
.facts{display:flex;gap:48px;padding:12px 0;border-bottom:1px solid var(--line);font-size:14px}
.facts span{display:flex;align-items:center;gap:14px}
.details p{margin-top:16px;font-size:14px;line-height:1.6;color:#444}
.actions{position:absolute;right:0;top:220px;display:flex;gap:12px}
.actions .dark{width:190px;height:34px}
.actions .gold{width:90px;height:34px}
/* pagination */
.pages{left:560px;top:2048px;display:flex;gap:6px;font-size:15px;align-items:center}
/* footer */
.footer{left:0;top:2108px;width:1200px;height:328px;background:var(--darker);color:#eee}
.footer .brand{position:absolute;left:112px;top:84px;margin:0;font-size:22px;gap:8px}
.footer .brand .sq{width:17px;height:17px}
.footer .socials{position:absolute;left:112px;top:150px;display:flex;gap:16px}
.fcol{position:absolute;top:60px}
.fcol h4{font-family:"Montserrat",sans-serif;font-size:30px;font-weight:700;margin-bottom:24px;letter-spacing:1px}
.fcol li{list-style:none;font-size:14px;margin-bottom:12px;display:flex;align-items:center;gap:12px;white-space:nowrap}
.news li{display:block;margin-bottom:14px;padding-left:12px;border-left:2px solid var(--gold)}
.news small{display:block;color:#aaa;font-size:12px}
</style>
</head>
<body>

<header class="abs topbar">
  <span class="item"><svg width="12" height="14" viewBox="0 0 12 14"><path d="M6 0a5 5 0 0 1 5 5c0 4-5 9-5 9S1 9 1 5a5 5 0 0 1 5-5z" fill="#d4a257"/></svg>18 Kampa Lane, Prague</span>
  <span class="item"><svg width="13" height="13" viewBox="0 0 13 13"><path d="M3 0l2 3-1.5 1.5a8 8 0 0 0 5 5L10 8l3 2-1.5 3C6 13 0 7 0 1.5z" fill="#d4a257"/></svg>(555) 010-2840</span>
  <span class="item"><svg width="15" height="11" viewBox="0 0 15 11"><rect x=".5" y=".5" width="14" height="10" fill="none" stroke="#d4a257"/><path d="M.5.5l7 6 7-6" fill="none" stroke="#d4a257"/></svg>hello@vltavasuites.com</span>
  <span class="spacer"></span>
  <span class="socials"><i class="dot"></i><i class="dot"></i><i class="dot"></i><i class="dot"></i><i class="dot"></i></span>
  <span>EN</span>
</header>

<nav class="abs nav">
  <a href="#">HOME</a><a href="#">APARTMENTS</a><a href="#">SERVICES</a>
  <span class="brand"><span class="sq"></span>Vltava Suites</span>
  <a href="#">TOURS</a><a href="#">GALLERY</a><a href="#">CONTACT</a>
</nav>

<div class="abs hero" role="img" aria-label="Bright loft apartment interior with wooden staircase"></div>

<form class="abs booking">
  <div class="field first">Check-in Date<div class="box" style="width:140px"></div></div>
  <div class="field">Check out date<div class="box" style="width:140px"></div></div>
  <div class="field">Adults<div class="box" style="width:80px">▾</div></div>
  <div class="field">Children<div class="box" style="width:80px">▾</div></div>
  <div class="field">Infants<div class="box" style="width:80px">▾</div></div>
  <div class="field">Promo code<div class="box" style="width:120px"></div></div>
  <div class="btn gold" style="width:160px;height:30px">CHECK AVAILABILITY</div>
</form>

<div class="abs steps"><span>APARTMENTS &amp; RATES</span><span>STAY ENHANCEMENT</span><span>GUEST DETAILS</span><span>REVIEW</span><span>CHECKOUT</span></div>

<aside>
  <section class="abs panel" style="top:572px">
    <h3>YOUR STAY</h3>
    <div class="body">Checkin: 21-11-2017<br>Checkout: 27-11-2017<br><br>Adults: 2<br>Children: 0<br>Infants: 0
      <div class="linkline">Change details</div></div>
  </section>
  <section class="abs panel" style="top:828px">
    <h3>YOUR SELECTION</h3>
    <div class="body">1 apartment selected
      <div class="mini-photo" role="img" aria-label="Living room of the selected apartment" style="margin-top:8px"></div>
      <div style="font-family:Montserrat,sans-serif;font-weight:700;margin-top:8px">BRAND NEW LUXURY</div>
      <div style="display:flex;justify-content:space-between;align-items:center;margin-top:6px;font-size:13px"><span style="text-decoration:underline">Add more</span><span class="btn gold" style="width:80px;height:22px;font-size:11px">BOOK NOW</span></div>
    </div>
  </section>
  <section class="abs panel" style="top:1200px">
    <h3>LOCATION</h3>
    <div class="body">
      <div class="map" role="img" aria-label="City map of Prague with apartment locations"></div>
      <div class="search"><div class="in"></div><div class="btn gold" style="width:70px;height:28px;font-size:11px">SEARCH</div></div>
    </div>
  </section>
</aside>

<main>
  <article class="abs listing" style="top:572px">
    <div class="photo" role="img" aria-label="Luxury apartment living room"><span class="tag">AVAILABLE</span>
      <svg class="arrow" style="left:8px" width="14" height="24"><path d="M12 2L2 12l10 10" stroke="#fff" stroke-width="3" fill="none"/></svg>
      <svg class="arrow" style="right:8px" width="14" height="24"><path d="M2 2l10 10L2 22" stroke="#fff" stroke-width="3" fill="none"/></svg></div>
    <div class="thumbs" role="img" aria-label="Apartment room thumbnails"><div></div><div></div><div></div><div></div></div>
    <div class="details">
      <h2>BRAND NEW LUXURY APARTMENT</h2>
      <div class="facts">
        <span><svg width="26" height="16"><rect x="1" y="6" width="24" height="7" fill="#2a2a2a"/><rect x="1" y="1" width="3" height="14" fill="#2a2a2a"/><rect x="5" y="3" width="7" height="4" fill="#2a2a2a"/></svg>1</span>
        <span><svg width="16" height="18"><circle cx="8" cy="5" r="4" fill="#2a2a2a"/><path d="M1 18c0-5 3-7 7-7s7 2 7 7z" fill="#2a2a2a"/></svg>4</span>
        <span><svg width="18" height="18"><rect x="1" y="1" width="16" height="16" fill="none" stroke="#2a2a2a" stroke-width="2"/><path d="M5 5h8v8H5z" fill="#2a2a2a"/></svg>28M²</span>
      </div>
      <p>Lorem ipsum dolor sit amet, consectetur adipiscing elit. Nam causae neque lorem. Duis ad eget dolore, commodo lorem quis.</p>
      <div class="actions"><span class="btn dark">MORE INFORMATION</span><span class="btn gold">SELECT</span></div>
    </div>
  </article>

  <article class="abs listing" style="top:944px">
    <div class="photo" role="img" aria-label="Luxury apartment living room"><span class="tag">AVAILABLE</span>
      <svg class="arrow" style="left:8px" width="14" height="24"><path d="M12 2L2 12l10 10" stroke="#fff" stroke-width="3" fill="none"/></svg>
      <svg class="arrow" style="right:8px" width="14" height="24"><path d="M2 2l10 10L2 22" stroke="#fff" stroke-width="3" fill="none"/></svg></div>
    <div class="thumbs" role="img" aria-label="Apartment room thumbnails"><div></div><div></div><div></div><div></div></div>
    <div class="details">
      <h2>BRAND NEW LUXURY APARTMENT</h2>
      <div class="facts">
        <span><svg width="26" height="16"><rect x="1" y="6" width="24" height="7" fill="#2a2a2a"/><rect x="1" y="1" width="3" height="14" fill="#2a2a2a"/><rect x="5" y="3" width="7" height="4" fill="#2a2a2a"/></svg>1</span>
        <span><svg width="16" height="18"><circle cx="8" cy="5" r="4" fill="#2a2a2a"/><path d="M1 18c0-5 3-7 7-7s7 2 7 7z" fill="#2a2a2a"/></svg>4</span>
        <span><svg width="18" height="18"><rect x="1" y="1" width="16" height="16" fill="none" stroke="#2a2a2a" stroke-width="2"/><path d="M5 5h8v8H5z" fill="#2a2a2a"/></svg>28M²</span>
      </div>
      <p>Lorem ipsum dolor sit amet, consectetur adipiscing elit. Nam causae neque lorem. Duis ad eget dolore, commodo lorem quis.</p>
      <div class="actions"><span class="btn dark">MORE INFORMATION</span><span class="btn gold">SELECT</span></div>
    </div>
  </article>

  <article class="abs listing" style="top:1316px">
    <div class="photo" role="img" aria-label="Luxury apartment living room"><span class="tag">AVAILABLE</span>
      <svg class="arrow" style="left:8px" width="14" height="24"><path d="M12 2L2 12l10 10" stroke="#fff" stroke-width="3" fill="none"/></svg>
      <svg class="arrow" style="right:8px" width="14" height="24"><path d="M2 2l10 10L2 22" stroke="#fff" stroke-width="3" fill="none"/></svg></div>
    <div class="thumbs" role="img" aria-label="Apartment room thumbnails"><div></div><div></div><div></div><div></div></div>
    <div class="details">
      <h2>BRAND NEW LUXURY APARTMENT</h2>
      <div class="facts">
        <span><svg width="26" height="16"><rect x="1" y="6" width="24" height="7" fill="#2a2a2a"/><rect x="1" y="1" width="3" height="14" fill="#2a2a2a"/><rect x="5" y="3" width="7" height="4" fill="#2a2a2a"/></svg>1</span>
        <span><svg width="16" height="18"><circle cx="8" cy="5" r="4" fill="#2a2a2a"/><path d="M1 18c0-5 3-7 7-7s7 2 7 7z" fill="#2a2a2a"/></svg>4</span>
        <span><svg width="18" height="18"><rect x="1" y="1" width="16" height="16" fill="none" stroke="#2a2a2a" stroke-width="2"/><path d="M5 5h8v8H5z" fill="#2a2a2a"/></svg>28M²</span>
      </div>
      <p>Lorem ipsum dolor sit amet, consectetur adipiscing elit. Nam causae neque lorem. Duis ad eget dolore, commodo lorem quis.</p>
      <div class="actions"><span class="btn dark">MORE INFORMATION</span><span class="btn gold">SELECT</span></div>
    </div>
  </article>

  <article class="abs listing" style="top:1688px">
    <div class="photo" role="img" aria-label="Luxury apartment living room"><span class="tag">AVAILABLE</span>
      <svg class="arrow" style="left:8px" width="14" height="24"><path d="M12 2L2 12l10 10" stroke="#fff" stroke-width="3" fill="none"/></svg>
      <svg class="arrow" style="right:8px" width="14" height="24"><path d="M2 2l10 10L2 22" stroke="#fff" stroke-width="3" fill="none"/></svg></div>
    <div class="thumbs" role="img" aria-label="Apartment room thumbnails"><div></div><div></div><div></div><div></div></div>
    <div class="details">
      <h2>BRAND NEW LUXURY APARTMENT</h2>
      <div class="facts">
        <span><svg width="26" height="16"><rect x="1" y="6" width="24" height="7" fill="#2a2a2a"/><rect x="1" y="1" width="3" height="14" fill="#2a2a2a"/><rect x="5" y="3" width="7" height="4" fill="#2a2a2a"/></svg>1</span>
        <span><svg width="16" height="18"><circle cx="8" cy="5" r="4" fill="#2a2a2a"/><path d="M1 18c0-5 3-7 7-7s7 2 7 7z" fill="#2a2a2a"/></svg>4</span>
        <span><svg width="18" height="18"><rect x="1" y="1" width="16" height="16" fill="none" stroke="#2a2a2a" stroke-width="2"/><path d="M5 5h8v8H5z" fill="#2a2a2a"/></svg>28M²</span>
      </div>
      <p>Lorem ipsum dolor sit amet, consectetur adipiscing elit. Nam causae neque lorem. Duis ad eget dolore, commodo lorem quis.</p>
      <div class="actions"><span class="btn dark">MORE INFORMATION</span><span class="btn gold">SELECT</span></div>
    </div>
  </article>

  <nav class="abs pages"><span>1</span>|<span>2</span>|<span>3</span>|<span>4</span>|<span>5</span>|<span>6</span>|<span>7</span>|<span>8</span>|<span>9</span>|<span>10</span>
    <svg width="12" height="16" style="margin-left:20px"><path d="M2 2l7 6-7 6" stroke="#2a2a2a" stroke-width="2" fill="none"/></svg></nav>
</main>

<footer class="abs footer">
  <span class="brand"><span class="sq"></span>Vltava Suites</span>
  <div class="socials"><i class="dot"></i><i class="dot"></i><i class="dot"></i><i class="dot"></i><i class="dot"></i></div>
  <div class="fcol" style="left:400px"><h4>CONTACT</h4><ul>
    <li><svg width="13" height="13" viewBox="0 0 13 13"><path d="M3 0l2 3-1.5 1.5a8 8 0 0 0 5 5L10 8l3 2-1.5 3C6 13 0 7 0 1.5z" fill="#d4a257"/></svg>(555) 010-2840</li>
    <li><svg width="15" height="11" viewBox="0 0 15 11"><rect x=".5" y=".5" width="14" height="10" fill="none" stroke="#d4a257"/><path d="M.5.5l7 6 7-6" fill="none" stroke="#d4a257"/></svg>hello@vltavasuites.com</li>
    <li><svg width="12" height="14" viewBox="0 0 12 14"><path d="M6 0a5 5 0 0 1 5 5c0 4-5 9-5 9S1 9 1 5a5 5 0 0 1 5-5z" fill="#d4a257"/></svg>18 Kampa Lane, Prague</li></ul></div>
  <div class="fcol" style="left:720px"><h4>LINKS</h4><ul>
    <li>Home</li><li>Services</li><li>Amenities</li><li>For Families</li><li>Tours &amp; Offers</li><li>About us</li></ul></div>
  <div class="fcol news" style="left:944px"><h4>NEWS</h4><ul>
    <li><small>14/11/2017</small>Lorem ipsum date sit</li>
    <li><small>14/11/2017</small>Lorem ipsum date sit</li>
    <li><small>14/11/2017</small>Lorem ipsum date sit</li></ul></div>
</footer>

</body>
</html>
```